website for local kavenda practicioner and yoga teacher trainer

The website should function primarily as:
A place where people can discover Kavenda and book sessions.
A central hub connecting all of my work.
A professional home that reflects my personality and approach.
Website design for Liesbet Oonwerk — Kavenda® Structural Integration practitioner, movement educator, yoga teacher and teacher trainer.
A website that can grow with future projects.
The website should feel: Warm, Human, Invitational, Professional, Accessible, Intelligent, Calm, Clear, Playful, Exploratory, Trustworthy
Avoid: New age aesthetics, Mystical clichés, Excessive spirituality, ”Guru" vibes, Overly clinical design, Corporate wellness branding, Busy layouts
Think: modern, grounded, curious and real.
My work combines three interconnected areas:
1.Bodywork: Touch, structure, awareness and one-on-one support.
2. Movement: Yoga, Pilates and embodied movement.
3. Education: Teacher trainings, workshops and continued learning.
Underlying values:
Curiosity over certainty
Possibility over perfection
Complexity without overwhelm
Science and lived experience together
Exploration rather than dogma
Human beings before methods
The primary goal of the website is to introduce people to Kavenda® Structural Integration and make it easy for them to:
Understand what Kavenda is
Discover whether it might be relevant for them
Learn what to expect from a session
Book an appointment
Booking should always feel visible and easy.
Secondary Goal: Present all other aspects of my work in one coherent place:
Yoga classes
Pilates classes
Teacher trainings
Workshops
Retreats
One-on-one movement sessions
Collaborations with studios
Website Structure
1: HOME
1.1.Hero Section: Large welcoming image
1.2 Two Main Pathways
- Bodywork: Kavenda® Structural Integration
- Movement & Education: Yoga, Pilates, trainings, workshops and retreats
- About Preview: Small introduction with portrait. + Button:
Read More
1.3 Current Events / What's Coming Up: Upcoming trainings, workshops and retreats. (This section should be easy to update)
1.4. Contact / Newsletter: Simple contact information
2: Kavenda® Structural Integration
What is Kavenda?
For whom is it?
What does a session look like?
FAQ
Prices
Booking
Future possibility:
Kaven Movement sessions
3: Movement
- Introductory text.
- Studio Classes (link to “my home base” - > local yoga studio)
- One-to-One Sessions: booking option (this is small; not a key aspect I want to promote)
- Workshops/ Retreats / Teacher Trainings => This section should be flexible and easy to update. Visitors should be able to click into specific offerings.
4. Events
Dynamic page for: Teacher trainings, Retreats, Workshops (see section in movement; here more elaborate)
Each event should contain: Image, Short description, Location, Date, Button for more information. (Linking to hosting studio/location)
5. Work With Me
For studios, organisations and teacher training schools.
Examples: Guest teaching, Workshops, Anatomy, Sequencing, Teacher development , Continuing education -> Clear call-to-action.
Call to action!!=> Book a Session
Prominent button in the navigation.
Footer:
- About Me: Longer biography (6th page)
Personal story and background.
- Testimonials (7th page): Separate page containing testimonials from:
Kavenda clients
Students
Teacher trainees
- Contact: 8th page
Visual Direction
Natural textures. Lots of white space.Editorial feeling.Professional photography.Simple navigation.
Less "wellness influencer.” More:Thoughtful, Contemporary, Timeless, Grounded, Human
Photography should show:
Teaching
Hands-on work
Natural movement
Real interaction
Simplicity
Avoid stereotypical yoga imagery and overly spiritual aesthetics.
Keywords
Warm. Curious. Human. Professional. Embodied. Intelligent. Accessible. Playful. Grounded. Exploratory. Real.
Inspiration / Core Message
Helping people feel more at home in their bodies through touch, movement and education.
The website should communicate that these are not separate services, but different expressions of the same intention:
Bodywork • Movement • Education.
Colours:
light orange/beige: e3d5c4
light orange/off white: f9f7f3
gray azure: 556b78
orange: d07b5a
grey orange: c09f80
dark grey: 3e3e3e
dark gray cyan 2f4f4f
gray green colour: a7c4a0
Fonts: Montserrat and Poppins + raleway
In added documents a try out idea of a website + logo. I will mainly use the logo with diffrent colours (image next to text).
My audience consists of people who want to feel more at home in their bodies and who appreciate a thoughtful, grounded and human approach to movement, touch and education. (30-65yo)
wellbeing
5+ page
- montserrat, poppins, raleway

```html
<!DOCTYPE html>
<html lang="en">
<head>
<meta charset="utf-8">
<title>Liesbet Oonwerk — Yoga & Bodywork</title>
<link href="https://fonts.googleapis.com/css2?family=Montserrat:ital,wght@0,400;0,500;0,600;1,400&family=Raleway:wght@300;400;500&display=swap" rel="stylesheet">
<style>
:root{
  --sand:#e3d5c4;
  --paper:#f9f7f3;
  --band:#f0e7de;
  --quote-bg:#f3ece5;
  --azure:#556b78;
  --orange:#d07b5a;
  --grey-orange:#c09f80;
  --ink:#3e3e3e;
  --cyan-dark:#2f4f4f;
  --green-bg:#e0e9da;
  --muted:#8a8580;
  --line:#e4dcd2;
}
*{margin:0;padding:0;box-sizing:border-box}
html,body{width:1200px;height:3198px;overflow:hidden;background:var(--paper)}
body{font-family:"Raleway",sans-serif;color:var(--ink);position:relative}
section,header,footer{position:absolute;left:0;width:1200px}
.abs{position:absolute}
.eyebrow{font-family:"Montserrat",sans-serif;font-size:8px;letter-spacing:2px;text-transform:uppercase;font-weight:500;color:var(--muted)}
.eyebrow.accent{color:var(--orange)}
h1,h2,h3{font-family:"Montserrat",sans-serif;font-weight:500;color:var(--azure)}
.body-text{font-size:11px;font-weight:300;line-height:1.6;color:var(--muted)}
.link{font-family:"Montserrat",sans-serif;font-size:10.5px;color:var(--ink);text-decoration:none;border-bottom:1px solid var(--ink);padding-bottom:2px}
.btn{font-family:"Montserrat",sans-serif;font-weight:600;font-size:10px;color:#fff;background:var(--orange);display:flex;align-items:center;justify-content:center;border-radius:2px}
.photo{border-radius:1px}

/* header */
.site-header{top:0;height:62px}
.brand{left:175px;top:0;width:196px;height:52px;background:#fff;display:flex;align-items:center;justify-content:center;gap:8px}
.brand-dot{width:14px;height:14px;border-radius:50%;background:var(--orange)}
.brand-name{font-family:"Montserrat",sans-serif;font-size:15px;font-weight:500;color:var(--ink)}
.nav{left:393px;top:20px;display:flex;gap:21px;font-family:"Montserrat",sans-serif;font-size:7.5px;letter-spacing:1.4px;color:var(--ink)}
.nav .lang{color:var(--grey-orange)}
.nav-cta{left:875px;top:10px;width:100px;height:30px}

/* hero */
.hero{top:62px;height:508px}
.hero h1{left:225px;top:124px;font-size:42px;line-height:1;width:340px;letter-spacing:-.3px}
.hero-photo{left:548px;top:27px;width:427px;height:400px;background:linear-gradient(135deg,#d8b98f,#c9a98a 50%,#8d6d55)}

/* pathways */
.pathways{top:570px;height:725px;background:var(--band);border-top:1px solid var(--line)}
.pathways h2{left:225px;top:100px;font-size:31px;line-height:1;width:450px}
.path-title{font-size:19px}

/* about */
.about{top:1295px;height:484px;border-top:1px solid var(--line)}
.about-photo{left:225px;top:80px;width:295px;height:324px;background:linear-gradient(160deg,#e3cfb4,#b9784f 60%,#8a4a2e)}
.about-word{left:660px;top:108px;font-family:"Montserrat",sans-serif;font-weight:600;font-size:98px;line-height:1;color:#e7ddd2;letter-spacing:-2px}

/* quote */
.quote{top:1779px;height:296px;background:var(--quote-bg);border-top:1px solid var(--line);text-align:center}
.quote blockquote{position:absolute;left:330px;width:540px;top:111px;font-family:"Montserrat",sans-serif;font-style:italic;font-size:30px;line-height:1.2;color:var(--cyan-dark)}

/* events */
.events{top:2075px;height:517px;border-top:1px solid var(--line)}
.event-photo{top:162px;width:237px;height:162px}
.event-title{font-size:13px;color:var(--ink);line-height:1.35;width:230px}
.event-meta{font-size:9px;color:var(--muted);font-weight:400}

/* newsletter */
.newsletter{top:2592px;height:385px;background:var(--green-bg);text-align:center}
.newsletter h2{position:absolute;left:350px;width:500px;top:102px;font-size:31px;line-height:1.1;color:var(--cyan-dark)}
.input{left:460px;top:237px;width:195px;height:28px;background:#fff;border:1px solid #d6d2c8;font-size:9px;color:#aaa;display:flex;align-items:center;padding-left:10px}

/* footer */
.site-footer{top:2977px;height:221px}
.foot-head{font-family:"Montserrat",sans-serif;font-size:8px;letter-spacing:1.6px;color:var(--muted)}
.foot-list{font-family:"Montserrat",sans-serif;font-size:9px;line-height:20px;color:var(--ink);list-style:none}
.legal{top:179px;left:0;width:1200px;border-top:1px solid var(--line);height:42px;font-size:7.5px;color:var(--muted)}
</style>
</head>
<body>

<header class="site-header">
  <div class="abs brand"><span class="brand-dot"></span><span class="brand-name">Liesbet Oonwerk</span></div>
  <nav class="abs nav">
    <span>KAVENDA</span><span>MOVEMENT</span><span>EVENTS</span><span>WORK WITH ME</span><span>ABOUT</span><span>TESTIMONIALS</span><span class="lang">EN · NL · FR</span>
  </nav>
  <a class="abs btn nav-cta">Book a Session</a>
</header>

<section class="hero">
  <p class="abs eyebrow accent" style="left:225px;top:98px">Kavenda · Movement · Education</p>
  <h1 class="abs">Feel more at<br>home<br>in your body.</h1>
  <p class="abs body-text" style="left:225px;top:267px;width:280px">Bodywork, movement and education — three doors into the same exploration.</p>
  <a class="abs btn" style="left:225px;top:326px;width:110px;height:34px">Book a Session</a>
  <a class="abs link" style="left:353px;top:336px">Discover Kavenda →</a>
  <svg class="abs" style="left:225px;top:390px" width="76" height="12"><path d="M1 7 C20 1 45 1 75 6" stroke="var(--grey-orange)" fill="none"/></svg>
  <div class="abs photo hero-photo" role="img" aria-label="Practitioner's hands resting on a client's shoulder in a sunlit room"></div>
</section>

<section class="pathways">
  <p class="abs eyebrow" style="left:225px;top:82px">Two pathways</p>
  <h2 class="abs">Two ways in, both rooted in the same curiosity.</h2>
  <p class="abs body-text" style="left:225px;top:174px;width:400px">The body is not something to perfect or control, but something to listen to, explore, and live within.</p>

  <div class="abs photo" style="left:225px;top:249px;width:355px;height:223px;background:linear-gradient(135deg,#e4c79d,#c99e78 55%,#9d7358)" role="img" aria-label="Hands-on bodywork at the shoulder"></div>
  <p class="abs eyebrow accent" style="left:225px;top:489px">Bodywork</p>
  <h3 class="abs path-title" style="left:225px;top:506px">Kavenda® Structural Integration</h3>
  <p class="abs body-text" style="left:225px;top:540px;width:270px;font-size:10px">A collaborative process exploring posture, movement, breath, and your relationship to gravity through touch and awareness.</p>
  <a class="abs link" style="left:225px;top:604px">Explore Kavenda →</a>

  <div class="abs photo" style="left:620px;top:289px;width:355px;height:223px;background:linear-gradient(135deg,#cfcbc0,#a9977c 55%,#6f5a45)" role="img" aria-label="Person moving freely in a bright studio"></div>
  <p class="abs eyebrow accent" style="left:620px;top:529px">Movement &amp; Education</p>
  <h3 class="abs path-title" style="left:620px;top:546px">Yoga, Pilates, Trainings &amp; Retreats</h3>
  <p class="abs body-text" style="left:620px;top:580px;width:270px;font-size:10px">Group classes, private sessions, trainings and retreats — movement as exploration, not performance.</p>
  <a class="abs link" style="left:620px;top:628px">Explore Movement →</a>
</section>

<section class="about">
  <div class="abs photo about-photo" role="img" aria-label="Portrait of the teacher seated cross-legged on a mat"></div>
  <div class="abs about-word" aria-hidden="true">about</div>
  <p class="abs eyebrow" style="left:570px;top:133px">About</p>
  <h2 class="abs" style="left:570px;top:152px;font-size:29px">Curiosity over certainty.</h2>
  <p class="abs body-text" style="left:570px;top:202px;width:365px;color:#6f6a66">At the heart of my work is the belief that our bodies are not machines to optimise, but living, sensing systems full of intelligence, adaptability and possibility.</p>
  <p class="abs body-text" style="left:570px;top:264px;width:360px;font-size:10px">Based in Leiden, I offer group classes, trainings, retreats and one-on-one sessions in movement and bodywork — locally and abroad. I work in English, Dutch and French.</p>
  <a class="abs link" style="left:570px;top:330px">More about me →</a>
</section>

<section class="quote">
  <svg class="abs" style="left:563px;top:79px" width="76" height="10"><path d="M1 6 C20 1 45 1 75 5" stroke="var(--grey-orange)" fill="none"/></svg>
  <blockquote>"Bodies are plastic to the intent of life."</blockquote>
  <p class="abs eyebrow" style="left:0;width:1200px;top:205px">Mira Tolvane</p>
</section>

<section class="events">
  <p class="abs eyebrow" style="left:225px;top:85px">Calendar</p>
  <h2 class="abs" style="left:225px;top:101px;font-size:31px">What's coming up.</h2>
  <a class="abs link" style="left:890px;top:122px">View all events →</a>

  <div class="abs photo event-photo" style="left:225px;background:linear-gradient(135deg,#b89c7e,#8d6e55 55%,#4f4540)" role="img" aria-label="Group teacher training session in a studio"></div>
  <p class="abs eyebrow accent" style="left:225px;top:337px">Teacher Training</p>
  <h3 class="abs event-title" style="left:225px;top:352px">200hr Yoga Teacher Training</h3>
  <p class="abs event-meta" style="left:225px;top:377px">March – November 2027 · Leiden, NL</p>
  <a class="abs link" style="left:225px;top:401px;font-size:9px">Learn more →</a>

  <div class="abs photo event-photo" style="left:481px;background:linear-gradient(135deg,#e8cfa8,#c9a47c 55%,#a37d5c)" role="img" aria-label="Treatment room with a table and plant"></div>
  <p class="abs eyebrow accent" style="left:481px;top:337px">Retreat</p>
  <h3 class="abs event-title" style="left:481px;top:352px">Spring Movement &amp; Bodywork Retreat</h3>
  <p class="abs event-meta" style="left:481px;top:395px">April 17 – 21, 2027 · Provence, France</p>
  <a class="abs link" style="left:481px;top:419px;font-size:9px">Learn more →</a>

  <div class="abs photo event-photo" style="left:738px;background:linear-gradient(135deg,#e7d8c4,#b7a38c 55%,#6d6660)" role="img" aria-label="Workshop participants seated in a circle"></div>
  <p class="abs eyebrow accent" style="left:738px;top:337px">Workshop</p>
  <h3 class="abs event-title" style="left:738px;top:352px">Anatomy of Breath</h3>
  <p class="abs event-meta" style="left:738px;top:377px">February 8, 2027 · Amsterdam, NL</p>
  <a class="abs link" style="left:738px;top:401px;font-size:9px">Learn more →</a>
</section>

<section class="newsletter">
  <p class="abs eyebrow" style="left:0;width:1200px;top:84px;color:var(--cyan-dark)">Stay in touch</p>
  <h2>Questions, or curious what's next?</h2>
  <p class="abs body-text" style="left:380px;width:440px;top:180px">Get in touch about Kavenda, classes and upcoming trainings — or leave your email to hear when something new opens up.</p>
  <div class="abs input">your@email.com</div>
  <a class="abs btn" style="left:663px;top:237px;width:77px;height:28px">Subscribe</a>
  <p class="abs eyebrow" style="left:0;width:1200px;top:300px">Leiden, NL · EN · NL · FR</p>
</section>

<footer class="site-footer">
  <div class="abs" style="left:198px;top:26px;width:114px;height:57px;background:#fff;display:flex;flex-direction:column;align-items:center;justify-content:center;gap:6px">
    <span class="brand-dot"></span><span class="brand-name" style="font-size:11px">Liesbet Oonwerk</span>
  </div>
  <p class="abs body-text" style="left:225px;top:89px;font-size:8.5px">Leiden, The Netherlands<br>Working in English, Dutch and French</p>
  <svg class="abs" style="left:225px;top:130px" width="76" height="10"><path d="M1 6 C20 1 45 1 75 5" stroke="var(--grey-orange)" fill="none"/></svg>
  <p class="abs foot-head" style="left:485px;top:43px">PRACTICE</p>
  <ul class="abs foot-list" style="left:485px;top:56px">
    <li>Kavenda® Structural Integration</li><li>Movement &amp; Classes</li><li>Trainings &amp; Retreats</li><li>Work With Me</li>
  </ul>
  <p class="abs foot-head" style="left:745px;top:43px">MORE</p>
  <ul class="abs foot-list" style="left:745px;top:56px">
    <li>About</li><li>Testimonials</li><li>Contact</li><li>Book a Session</li>
  </ul>
  <div class="abs legal">
    <span class="abs" style="left:225px;top:17px">© 2026 Liesbet Oonwerk. All rights reserved.</span>
    <span class="abs" style="right:225px;top:17px">Kavenda® is a registered service mark of the Tolvane Institute®.</span>
  </div>
</footer>

</body>
</html>
```